Surface Protection company needs cards

We are a New Zealand company that will apply nanotechnology coatings on surfaces to prevent growth and spread of bacteria, viruses, mold etc with a sprayer. We deal with large corporates, airlines, hospitals and schools so we are after a new modern, simple and clean look that will have great visual impact.
We a company that is focused on prevention and protection.

Company name, Vela Shield

Subtext, Antimicrobial Surface Protection

Logo, VS

Target Market(s)

Hospitals, Transport agencies, Airlines, Corporate entities

Contact Information for Business Card

Company name, VelaShield
Logo, VS

Gareth Tolley
velashieldnz@postbox.example
+64219305562
www.velashield.example.nz

Requirements
Must have
• Simple clean look.
Nice to have
• We apply nano coatings so try and incorporate this into a theme somehow

```html
<!DOCTYPE html>
<html lang="en">
<head>
<meta charset="utf-8">
<title>Vela Shield — Business Card</title>
<link href="https://fonts.googleapis.com/css2?family=Questrial&display=swap" rel="stylesheet">
<style>
  :root {
    --canvas: #1c1c1e;
    --card-light: #f4f4f4;
    --card-dark: #161616;
    --ink-dark: #2a2a2a;
    --ink-mid: #8a8a8a;
    --ink-light: #bdbdbd;
    --mark-dot: #777777;
  }
  * { margin: 0; padding: 0; box-sizing: border-box; }
  html, body {
    width: 1200px; height: 900px; overflow: hidden;
    background: var(--canvas);
    font-family: "Questrial", sans-serif;
  }
  .sheet {
    width: 1200px; height: 900px;
    display: flex; flex-direction: column;
    align-items: center; justify-content: center; gap: 50px;
  }
  .card {
    width: 620px; height: 354px;
    border-radius: 26px;
    position: relative;
  }
  .card--front { background: var(--card-light); color: var(--ink-dark); }
  .card--back { background: var(--card-dark); color: var(--ink-light); }

  .brand {
    display: flex; align-items: center; gap: 14px;
    font-size: 52px; letter-spacing: 0.5px; line-height: 1;
  }
  .brand__dot {
    width: 26px; height: 26px; border-radius: 50%;
    border: 3px solid var(--mark-dot);
  }
  .card--front .brand { position: absolute; left: 150px; top: 52px; color: var(--ink-dark); }
  .card--back .brand { position: absolute; left: 120px; top: 112px; color: var(--ink-light); }

  .person { position: absolute; left: 190px; top: 148px; }
  .person__name { font-size: 22px; letter-spacing: 4px; text-transform: uppercase; color: var(--ink-dark); }
  .person__role { font-size: 17px; letter-spacing: 1.5px; color: var(--ink-mid); margin-top: 2px; }
  .person__rule { width: 18px; height: 3px; background: var(--ink-dark); margin: 14px 0 0 118px; }

  .contact { position: absolute; left: 110px; top: 228px; font-size: 18px; line-height: 1.55; color: var(--ink-dark); }
  .contact__phone { padding-left: 82px; }
  .contact__web span { color: var(--ink-mid); }

  .tagline {
    position: absolute; left: 124px; top: 200px;
    font-size: 18px; letter-spacing: 2px; color: var(--ink-light);
  }
</style>
</head>
<body>
  <main class="sheet">
    <section class="card card--front">
      <div class="brand"><span class="brand__dot"></span><span class="brand__name">Vela Shield</span></div>
      <div class="person">
        <p class="person__name">Gareth Tolley</p>
        <p class="person__role">Managing Director</p>
        <div class="person__rule"></div>
      </div>
      <div class="contact">
        <p class="contact__phone">+64 219 305 562</p>
        <p class="contact__email">velashieldnz@postbox.example</p>
        <p class="contact__web">www.<span>velashield.example.nz</span></p>
      </div>
    </section>

    <section class="card card--back">
      <div class="brand"><span class="brand__dot"></span><span class="brand__name">Vela Shield</span></div>
      <p class="tagline">Antimicrobial Surface Protection</p>
    </section>
  </main>
</body>
</html>
```